Specialised investor in e-mobility and energy wants business card design

We need a business card design that fits our existing corporate design. <The look and feel must be 'sharp'/'clean', dynamic, communicate momentum, professionalism etc (as one would imagine from a firm in the financial sector). We like the idea of a reverse-side of the card that includes the logo, and the name and contact details on the other. We expect the deliverable to be whatever format might be required to be able to get cards printed directly by a service such as tandor press. Our website is www.orm.capital

```html
<!DOCTYPE html>
<html lang="en">
<head>
<meta charset="utf-8">
<title>ORM Capital – Business Card</title>
<link href="https://fonts.googleapis.com/css2?family=Roboto:wght@400;700&display=swap" rel="stylesheet">
<style>
  :root {
    --backdrop: #d3d4d6;
    --forest: #36532a;
    --forest-light: #3d5f2d;
    --leaf: #7cb342;
    --ink: #2b3a22;
    --paper: #f6f8f1;
    --white: #ffffff;
  }
  html, body {
    margin: 0;
    width: 900px;
    height: 1200px;
    overflow: hidden;
    background: var(--backdrop);
    font-family: "Roboto", sans-serif;
  }
  .card {
    position: absolute;
    left: 165px;
    width: 571px;
    height: 374px;
  }
  .card-front {
    top: 190px;
    background: radial-gradient(ellipse at 50% 85%, var(--forest-light), var(--forest) 70%);
    display: flex;
    align-items: center;
    justify-content: center;
  }
  .brand-name {
    color: var(--white);
    font-weight: 400;
    font-size: 56px;
    letter-spacing: 1px;
    display: flex;
    align-items: center;
    gap: 14px;
    margin-top: -10px;
  }
  .brand-dot {
    width: 16px;
    height: 16px;
    border-radius: 50%;
    background: var(--white);
  }
  .card-back {
    top: 636px;
    background: var(--paper);
  }
  .identity {
    position: absolute;
    right: calc(571px - 268px);
    top: 150px;
    text-align: right;
  }
  .person-name {
    color: var(--leaf);
    font-weight: 700;
    font-size: 23px;
    line-height: 1.2;
  }
  .person-role {
    color: var(--ink);
    font-size: 13px;
    margin-top: 2px;
    letter-spacing: 0.5px;
  }
  .divider {
    position: absolute;
    left: 284px;
    top: 158px;
    width: 2px;
    height: 58px;
    background: var(--ink);
  }
  .contacts {
    position: absolute;
    left: 302px;
    top: 154px;
    margin: 0;
    padding: 0;
    list-style: none;
  }
  .contacts li {
    display: flex;
    align-items: center;
    height: 22px;
    color: var(--ink);
    font-size: 14px;
    letter-spacing: 0.6px;
  }
  .contacts svg {
    width: 11px;
    height: 11px;
    margin-right: 8px;
    fill: var(--leaf);
  }
</style>
</head>
<body>
  <section class="card card-front">
    <div class="brand-name"><span class="brand-dot"></span>ORM Capital</div>
  </section>

  <section class="card card-back">
    <div class="identity">
      <div class="person-name">Paul Hendry</div>
      <div class="person-role">Partner</div>
    </div>
    <div class="divider"></div>
    <ul class="contacts">
      <li>
        <svg viewBox="0 0 24 24" aria-hidden="true"><path d="M6.6 10.8a15.1 15.1 0 0 0 6.6 6.6l2.2-2.2a1 1 0 0 1 1-.25 11.4 11.4 0 0 0 3.6.57 1 1 0 0 1 1 1V20a1 1 0 0 1-1 1A17 17 0 0 1 3 4a1 1 0 0 1 1-1h3.5a1 1 0 0 1 1 1c0 1.25.2 2.45.57 3.57a1 1 0 0 1-.25 1z"/></svg>
        +41 79415 2087
      </li>
      <li>
        <svg viewBox="0 0 24 24" aria-hidden="true"><path d="M2 5h20v14H2z M3 6l9 7 9-7" fill="none" stroke="#7cb342" stroke-width="2.5"/><path d="M2 5h20v14H2z"/><path d="M3 6l9 7 9-7" fill="none" stroke="#f6f8f1" stroke-width="1.8"/></svg>
        paul@orm.capital
      </li>
      <li>
        <svg viewBox="0 0 24 24" aria-hidden="true"><circle cx="12" cy="12" r="10" fill="none" stroke="#7cb342" stroke-width="2"/><ellipse cx="12" cy="12" rx="4" ry="10" fill="none" stroke="#7cb342" stroke-width="2"/><path d="M2 12h20M4 7h16M4 17h16" stroke="#7cb342" stroke-width="1.6"/></svg>
        www.orm.capital
      </li>
    </ul>
  </section>
</body>
</html>
```